7 page website for Dog Training Business

we are seeking a website design that should be 7 pages for a Las Vegas Dog training business. the site will have a heavy focus on video, and social media. Ideas design can be borrowed from http://plumcrestway.net
attached is a copy of the logo and business card mock up. Content is currently being written and will be posted shortly

Training

```html
<!DOCTYPE html>
<html lang="en">
<head>
<meta charset="utf-8">
<title>Kestrel Dog Training</title>
<link href="https://fonts.googleapis.com/css2?family=Lato:wght@400;700&family=Raleway:wght@400;500&family=Caveat:wght@400&display=swap" rel="stylesheet">
<style>
:root{
  --grass:#6fa52a;
  --grass-dark:#4e8a1c;
  --brick:#8a2411;
  --brick-dark:#6e1c0c;
  --lime:#c7dd5a;
  --lime-text:#dbeb6c;
  --ink:#1d1d1d;
  --paper:#ffffff;
  --night:#000000;
}
*{margin:0;padding:0;box-sizing:border-box}
html,body{width:877px;height:1200px;overflow:hidden}
body{position:relative;font-family:'Lato',sans-serif;color:var(--ink);
  background:radial-gradient(ellipse at center,#8bc03c 0%,var(--grass) 55%,var(--grass-dark) 100%)}
.page{position:absolute;left:73px;top:0;width:733px;height:1040px;background:var(--paper)}
.abs{position:absolute}
.brand{left:19px;top:3px;display:flex;align-items:center;gap:6px}
.brand-ring{width:78px;height:78px;border-radius:50%;background:var(--lime);border:3px solid var(--brick);
  display:flex;align-items:center;justify-content:center;font-family:'Lato',sans-serif;font-weight:700;font-size:15px;color:var(--brick)}
.tagline{left:200px;top:10px;width:260px;text-align:center;font-family:'Caveat',cursive;font-size:31px;line-height:33px;color:#2f5a2a}
.social{display:flex;gap:7px}
.social span{width:23px;height:23px;border-radius:50%;background:var(--brick);display:block}
.social span:first-child{background:var(--lime)}
.header-social{left:604px;top:48px}
.nav-ribbon{position:absolute;left:4px;top:94px;width:869px;height:34px;background:var(--brick-dark);clip-path:polygon(0 50%,2% 0,98% 0,100% 50%,98% 100%,2% 100%)}
.nav-bar{position:absolute;left:47px;top:87px;width:785px;height:34px;background:var(--brick);box-shadow:0 3px 6px rgba(0,0,0,.35);border:2px solid #a23318}
.menu{display:flex;gap:22px;font-size:11.5px;font-weight:700;color:#fff;list-style:none}
.menu li:first-child{color:var(--lime-text)}
.nav-bar .menu{position:absolute;left:46px;top:8px}
.hero{left:18px;top:121px;width:695px;height:261px;background:linear-gradient(120deg,#9ab86a 0%,#c9a58c 40%,#6d5a3a 70%,#8fae5c 100%)}
.hero-caption{position:absolute;left:0;bottom:0;width:100%;height:46px;background:rgba(138,36,17,.82);color:#fff;font-weight:700;font-size:22px;padding:8px 8px}
.heading{display:flex;align-items:flex-end;gap:4px;font-family:'Raleway',sans-serif;font-size:18px;color:#222}
.heading b{font-weight:400;color:var(--brick)}
.heading .t{border-bottom:1px solid var(--brick);padding-bottom:3px}
.paw{width:26px;height:24px;flex:none}
.copy{font-size:8.2px;line-height:13.6px;color:#222}
.btn{display:inline-block;background:var(--brick);color:#fff;font-size:8.5px;padding:6px 11px}
.btn.lime{background:var(--lime);color:var(--brick);padding:5px 14px}
.quote-mark{font-family:Georgia,serif;font-size:22px;color:#222}
.avatar{left:623px;top:515px;width:66px;height:66px;border-radius:50%;background:linear-gradient(#caa07a,#8a2411)}
.services{left:18px;top:610px;display:flex;gap:20px}
.service{width:219px;height:213px;background:var(--brick);text-align:center;color:#fff;padding-top:18px;box-shadow:0 2px 3px rgba(0,0,0,.3)}
.service .ph{width:168px;height:91px;margin:0 auto 13px}
.service h3{font-size:9.5px;font-weight:700;margin-bottom:3px}
.service p{font-size:8px;line-height:13.8px;padding:0 20px;margin-bottom:7px}
.arrows{left:669px;top:864px;display:flex;gap:6px}
.arrows span{width:19px;height:18px;display:flex;align-items:center;justify-content:center}
.gallery{left:18px;top:889px;display:flex;gap:19px}
.gallery div{width:160px;height:116px}
.footer{position:absolute;left:0;top:1040px;width:877px;height:146px;background:var(--night);color:#fff}
.footer .heading{color:#fff}
.footer .heading b{color:#a8311a}
.contact-line{left:118px;top:62px;display:flex;align-items:center;gap:9px;font-size:9.6px}
.rule{left:91px;top:89px;width:695px;height:1px;background:#333}
.footer .menu{position:absolute;left:95px;top:109px}
.footer-band{position:absolute;left:0;top:1186px;width:877px;height:14px;background:var(--brick)}
</style>
</head>
<body>
<svg width="0" height="0" style="position:absolute">
  <defs>
    <symbol id="paw" viewBox="0 0 26 24">
      <ellipse cx="13" cy="17" rx="6.5" ry="5.5"/>
      <ellipse cx="4" cy="10" rx="3" ry="3.6"/>
      <ellipse cx="9.5" cy="4.5" rx="3" ry="3.8"/>
      <ellipse cx="16.5" cy="4.5" rx="3" ry="3.8"/>
      <ellipse cx="22" cy="10" rx="3" ry="3.6"/>
    </symbol>
  </defs>
</svg>

<div class="page">
  <div class="abs brand"><div class="brand-ring">Kestrel</div></div>
  <div class="abs tagline">Professional dog training services for you!</div>
  <div class="abs social header-social" aria-label="Social links"><span></span><span></span><span></span><span></span></div>

  <div class="abs hero" role="img" aria-label="Photo of a smiling woman with a small terrier outdoors">
    <div class="hero-caption">Everything You Need To get Started Right Away !</div>
  </div>

  <div class="abs heading" style="left:20px;top:403px">
    <svg class="paw" fill="#8a2411"><use href="#paw"/></svg>
    <span class="t">Welcome To <b>Kestrel Dog Training</b></span>
  </div>
  <p class="abs copy" style="left:20px;top:449px;width:340px">Duis autem vel eum iriure dolor in hendrerit in vulputate velit esse molestie consequat, vel illum dolore eu feugiat nulla facilisis at vero eros et accumsan et iusto odio dignissim qui blandit praesent luptatum zzril delenit augue duis dolore te feugait nulla facilisi.feugiat nulla facilisis at vero eros et accumsan et iusto .</p>
  <span class="abs btn" style="left:20px;top:518px">Read More</span>

  <div class="abs heading" style="left:377px;top:403px">
    <svg class="paw" fill="#8a2411"><use href="#paw"/></svg>
    <span class="t">What People <b>Say About Us</b></span>
  </div>
  <span class="abs quote-mark" style="left:381px;top:432px">“</span>
  <p class="abs copy" style="left:382px;top:451px;width:315px;line-height:17.5px;text-indent:10px">Duis autem vel eum iriure dolor in hendrerit in vulputate velit esse molestie consequat, vel illum dolore eu feugiat nulla facilisis at vero eros et accumsan et iusto odio dignissim qui blandit praesent luptatum zzril delenit</p>
  <span class="abs quote-mark" style="left:610px;top:495px">”</span>
  <div class="abs copy" style="left:570px;top:537px;text-align:right;font-size:9px">Mr.Dorran<br><span style="color:#8a2411">Director</span></div>
  <div class="abs avatar" role="img" aria-label="Portrait of the director"></div>

  <div class="abs heading" style="left:20px;top:567px">
    <svg class="paw" fill="#8a2411"><use href="#paw"/></svg>
    <span class="t">Our <b>Services</b></span>
  </div>
  <div class="abs services">
    <div class="service">
      <div class="ph" role="img" aria-label="Photo of a child and woman with a golden retriever" style="background:linear-gradient(120deg,#c9b79a,#e8e2d4,#6b5a44)"></div>
      <h3>IN-HOME TRAINING</h3>
      <p>putate velit esse molestie consequat, vel illum dolore eu feugiat nulla facilisis at vero eros et accumsan et iusto</p>
      <span class="btn lime">Read More</span>
    </div>
    <div class="service">
      <div class="ph" role="img" aria-label="Photo of a dog running on grass with a ball" style="background:linear-gradient(#2f4a2a,#3b6a2c 60%,#5c9a34)"></div>
      <h3>BOARD-AND-TRAIN PACKAGES</h3>
      <p>putate velit esse molestie consequat, vel illum dolore eu feugiat nulla facilisis at vero eros et accumsan et iusto</p>
      <span class="btn lime">Read More</span>
    </div>
    <div class="service">
      <div class="ph" role="img" aria-label="Photo of a dog leaping over an agility jump" style="background:linear-gradient(#8fb6d8,#b5cde0 45%,#4f7a34)"></div>
      <h3>PHONE CONSULTATION TRAINING</h3>
      <p>putate velit esse molestie consequat, vel illum dolore eu feugiat nulla facilisis at vero eros et accumsan et iusto</p>
      <span class="btn lime">Read More</span>
    </div>
  </div>

  <div class="abs heading" style="left:20px;top:843px">
    <svg class="paw" fill="#8a2411"><use href="#paw"/></svg>
    <span class="t">Our <b>Gallery</b></span>
  </div>
  <div class="abs arrows">
    <span style="background:#8a2411"><svg width="10" height="9" viewBox="0 0 10 9" fill="none" stroke="#fff" stroke-width="1.5"><path d="M5 1 1.5 4.5 5 8M9 1 5.5 4.5 9 8"/></svg></span>
    <span style="background:#000"><svg width="10" height="9" viewBox="0 0 10 9" fill="none" stroke="#fff" stroke-width="1.5"><path d="M1 1l3.5 3.5L1 8M5 1l3.5 3.5L5 8"/></svg></span>
  </div>
  <div class="abs gallery">
    <div role="img" aria-label="Photo of a puppy carrying a red toy" style="background:#b4624a;position:relative">
      <svg width="160" height="116" style="position:absolute;left:0;top:0">
        <circle cx="61" cy="57" r="12" fill="#e9d6cf"/><circle cx="92" cy="57" r="12" fill="#a9412c"/>
        <circle cx="60" cy="56" r="4" fill="none" stroke="#8a2411" stroke-width="1.6"/><path d="M63 59l3 3" stroke="#8a2411" stroke-width="1.6"/>
        <path d="M88 59l8-6" stroke="#fff" stroke-width="1.6"/>
      </svg>
    </div>
    <div role="img" aria-label="Photo of a dog jumping through an agility hoop" style="background:linear-gradient(#5e7a4a,#8a7a6a 50%,#4f8a3a)"></div>
    <div role="img" aria-label="Photo of a shepherd dog leaping a hurdle beside a trainer" style="background:linear-gradient(#cfd6dc,#e6e9ec 60%,#5a7a40)"></div>
    <div role="img" aria-label="Photo of a couple hugging a Bernese mountain dog" style="background:linear-gradient(120deg,#d9b49a,#3a2a24 50%,#e0c2ac)"></div>
  </div>
</div>

<div class="nav-ribbon"></div>
<nav class="nav-bar">
  <ul class="menu"><li>Home</li><li>About Us</li><li>Services</li><li>Photos/Videos</li><li>FAQ</li><li>Tips</li><li>Store</li><li>Contacts</li></ul>
</nav>

<footer class="footer">
  <div class="abs heading" style="left:92px;top:11px">
    <svg class="paw" fill="#fff"><use href="#paw"/></svg><span>Contact <b>Us</b></span>
  </div>
  <div class="abs heading" style="left:631px;top:11px">
    <svg class="paw" fill="#fff"><use href="#paw"/></svg><span>Stay <b>Connected</b></span>
  </div>
  <div class="abs contact-line">
    <svg width="10" height="14" viewBox="0 0 10 14"><path d="M5 0a5 5 0 0 0-5 5c0 4 5 9 5 9s5-5 5-9a5 5 0 0 0-5-5z" fill="#a8311a"/><circle cx="5" cy="5" r="1.8" fill="#000"/></svg>
    <span>412 Larkfield Lane Brennock, K07 31TS</span>
    <svg width="12" height="12" viewBox="0 0 12 12" style="margin-left:6px"><path d="M2 0l3 3-1.5 2A7 7 0 0 0 7 8.5L9 7l3 3-2 2C5 12 0 7 0 2z" fill="#a8311a"/></svg>
    <span>+1 800 555 0142</span>
    <svg width="15" height="11" viewBox="0 0 15 11" style="margin-left:8px"><rect width="15" height="11" fill="#a8311a"/><path d="M0 0l7.5 6L15 0" fill="none" stroke="#000" stroke-width="1.2"/></svg>
    <span>E-mail: hello@kestreldogs.net</span>
  </div>
  <div class="abs social" style="left:677px;top:58px"><span style="background:var(--brick)"></span><span></span><span></span><span></span></div>
  <div class="abs rule"></div>
  <ul class="menu"><li>Home</li><li>About Us</li><li>Services</li><li>Photos/Videos</li><li>FAQ</li><li>Tips</li><li>Store</li><li>Contacts</li></ul>
</footer>
<div class="footer-band"></div>
</body>
</html>
```